kiro dead see mud mask label design

Hi
looking for a nice label design for dead see mud mask for kiro beuty here is how other poepl are labeling it https://www.shopvarnel.com/TOP-Mineral-Clay-Pack/dp/Q71KWRPZNM/ref=sr_1_1_a_it?ie=UTF8&qid=1470950373&sr=8-1&keywords=dead+see+mud+mask
we attached are logo and the label from the mfr we want the colors on the albel gray and purple

```html
<!DOCTYPE html>
<html lang="en">
<head>
<meta charset="utf-8">
<title>kiro Dead Sea Mud Mask – label set</title>
<link rel="stylesheet" href="https://fonts.googleapis.com/css2?family=Questrial&family=Tinos:wght@400&family=Pinyon+Script&display=swap">
<style>
:root{
  --mauve:#a8659a;
  --mauve-light:#c9a3be;
  --slate:#5f5d5e;
  --ink:#4a3f47;
  --paper:#ffffff;
  --white:#ffffff;
}
*{box-sizing:border-box;margin:0;padding:0}
html,body{width:771px;height:1200px;overflow:hidden;background:var(--paper)}
body{position:relative;font-family:"Tinos",serif;color:var(--white)}
.label{position:absolute;width:244px;height:194px;display:flex;flex-direction:column;overflow:hidden}
.col-front{left:78px}
.col-back{left:424px}
.row-1{top:132px}
.row-2{top:524px}
.row-3{top:918px}
.band{display:flex;flex-direction:column;align-items:center;justify-content:center;text-align:center}
.mauve{background:var(--mauve);color:var(--white)}
.light{background:var(--mauve-light);color:var(--ink)}
.slate{background:var(--slate);color:var(--white)}
.kicker{font-size:9.5px;letter-spacing:.2px;margin-bottom:6px}
.brand{display:flex;align-items:center;gap:8px;font-family:"Questrial",sans-serif;font-size:24px;line-height:1}
.brand .dot{width:18px;height:18px;border:2px solid currentColor;border-radius:50%}
.brand.small{font-size:14px;gap:5px}
.brand.small .dot{width:11px;height:11px;border-width:1.5px}
.title{font-family:"Questrial",sans-serif;font-size:19px;line-height:1.1}
.title-sm{font-family:"Questrial",sans-serif;font-size:13px}
.script{font-family:"Pinyon Script",cursive;font-size:24px;line-height:1}
.tagline{font-size:8.6px;line-height:1.35;padding:0 14px}
.tagline.sans{font-family:"Questrial",sans-serif;font-size:9.2px}
.origin{font-size:7.6px;line-height:1.4}
.origin .weight{font-size:6.6px;opacity:.9}
.copy{font-size:6.9px;line-height:1.32;padding:0 6px}
.icons{display:flex;gap:12px;justify-content:center;margin:5px 0}
.ingredients{font-size:6.9px;line-height:1.32;padding:0 6px;text-align:left}
.grow{flex:1}
</style>
</head>
<body>

<!-- Front label, mauve and slate -->
<section class="label col-front row-1">
  <div class="band mauve" style="height:78px">
    <p class="kicker">Pure Natural &amp; Organic Cosmetics</p>
    <p class="brand"><span class="dot"></span>kiro</p>
  </div>
  <div class="band slate" style="height:74px">
    <h1 class="title">Dead Sea Mud Mask</h1>
    <p class="tagline" style="margin-top:8px">improve your skin's elasticity and minimize the appearance of pores for a flawless glow</p>
  </div>
  <div class="band mauve grow">
    <p class="origin">Made in Jordan<br><span class="weight">net wt. 40LB - 18.18kg</span></p>
  </div>
</section>

<!-- Back label, mauve -->
<section class="label col-back row-1">
  <div class="band mauve" style="height:30px"><p class="brand small"><span class="dot"></span>kiro</p></div>
  <div class="band light" style="height:22px"><h2 class="title-sm">Dead Sea Mud Mask</h2></div>
  <div class="band mauve grow">
    <p class="copy">Dead Sea Mud Mask pulls out the toxins and excess oils in your skin from diet and pollution. Nourishing oils like Sunflower, Jojoba &amp; Hickory Bark hydrates the skin, giving you a youthful appearance, reducing the look of fine lines and wrinkles. Say goodbye to acne blackheads, and breakouts and make your skin feeling deeply refreshed &amp; cleansed.</p>
    <div class="icons">
      <svg width="18" height="18" viewBox="0 0 18 18" fill="none" stroke="currentColor" stroke-width="1.4"><path d="M3 9a6 6 0 0 1 10.5-4M15 9a6 6 0 0 1-10.5 4"/><path d="M13.5 1.5v3.5H10M4.5 16.5V13H8"/></svg>
      <svg width="18" height="18" viewBox="0 0 18 18" fill="currentColor"><path d="M9 2l4 7H5z"/><path d="M3 12h12l-2 4H5z"/></svg>
      <svg width="18" height="18" viewBox="0 0 18 18" fill="none" stroke="currentColor" stroke-width="1.2"><rect x="3" y="6" width="12" height="10" rx="1"/><path d="M4 3h10v3H4z"/><text x="9" y="14" font-size="5" text-anchor="middle" fill="currentColor" stroke="none" font-family="sans-serif">18M</text></svg>
    </div>
    <p class="ingredients">Ingredients: Dead Sea Mud, Deionized Water, Kaolin, Allantoin, Shea Butter, Sunflower Oil, Aloe Vera Juice, Vegetable Glycerin, Jojoba Oil, Hickory Bark Extract, Calendula Oil, Xanthan Gum.</p>
  </div>
</section>

<!-- Front label, mauve with script title -->
<section class="label col-front row-2">
  <div class="band mauve" style="height:62px"><p class="brand"><span class="dot"></span>kiro</p></div>
  <div class="band light" style="height:70px">
    <p class="script">Dead Sea</p>
    <h1 class="title" style="font-size:24px">Mud Mask</h1>
  </div>
  <div class="band mauve grow">
    <p class="tagline sans">improve your skin's elasticity and minimize the appearance of pores for a flawless glow</p>
    <p class="origin" style="margin-top:6px">Made in Jordan<br><span class="weight">net wt. 40LB - 18.18kg</span></p>
  </div>
</section>

<!-- Back label, light mauve -->
<section class="label col-back row-2">
  <div class="band light" style="height:30px;color:var(--mauve)"><p class="brand small"><span class="dot"></span>kiro</p></div>
  <div class="band mauve" style="height:22px;color:var(--mauve-light)"><h2 class="title-sm">Dead Sea Mud Mask</h2></div>
  <div class="band light grow">
    <p class="copy">Dead Sea Mud Mask pulls out the toxins and excess oils in your skin from diet and pollution. Nourishing oils like Sunflower, Jojoba &amp; Hickory Bark hydrates the skin, giving you a youthful appearance, reducing the look of fine lines and wrinkles. Say goodbye to acne blackheads, and breakouts and make your skin feeling deeply refreshed &amp; cleansed.</p>
    <div class="icons">
      <svg width="18" height="18" viewBox="0 0 18 18" fill="none" stroke="currentColor" stroke-width="1.4"><path d="M3 9a6 6 0 0 1 10.5-4M15 9a6 6 0 0 1-10.5 4"/><path d="M13.5 1.5v3.5H10M4.5 16.5V13H8"/></svg>
      <svg width="18" height="18" viewBox="0 0 18 18" fill="currentColor"><path d="M9 2l4 7H5z"/><path d="M3 12h12l-2 4H5z"/></svg>
      <svg width="18" height="18" viewBox="0 0 18 18" fill="none" stroke="currentColor" stroke-width="1.2"><rect x="3" y="6" width="12" height="10" rx="1"/><path d="M4 3h10v3H4z"/><text x="9" y="14" font-size="5" text-anchor="middle" fill="currentColor" stroke="none" font-family="sans-serif">18M</text></svg>
    </div>
    <p class="ingredients">Ingredients: Dead Sea Mud, Deionized Water, Kaolin, Allantoin, Shea Butter, Sunflower Oil, Aloe Vera Juice, Vegetable Glycerin, Jojoba Oil, Hickory Bark Extract, Calendula Oil, Xanthan Gum.</p>
  </div>
</section>

<!-- Front label, light mauve and slate -->
<section class="label col-front row-3" style="height:204px">
  <div class="band light" style="height:76px;color:var(--ink)">
    <p class="kicker">Pure Natural &amp; Organic Cosmetics</p>
    <p class="brand" style="color:var(--mauve)"><span class="dot"></span>kiro</p>
  </div>
  <div class="band slate" style="height:94px">
    <h1 class="title" style="font-size:22px;color:var(--mauve-light)">Dead Sea<br>Mud Mask</h1>
    <p class="tagline" style="margin-top:6px;color:var(--mauve-light)">improve your skin's elasticity and minimize the appearance of pores for a flawless glow</p>
  </div>
  <div class="band light grow">
    <p class="origin" style="color:var(--white)">Made in Jordan<br><span class="weight">net wt. 40LB - 18.18kg</span></p>
  </div>
</section>

<!-- Back label, slate -->
<section class="label col-back row-3">
  <div class="band slate" style="height:30px"><p class="brand small"><span class="dot" style="border-color:var(--mauve)"></span>kiro</p></div>
  <div class="band light" style="height:22px"><h2 class="title-sm">Dead Sea Mud Mask</h2></div>
  <div class="band slate grow">
    <p class="copy">Dead Sea Mud Mask pulls out the toxins and excess oils in your skin from diet and pollution. Nourishing oils like Sunflower, Jojoba &amp; Hickory Bark hydrates the skin, giving you a youthful appearance, reducing the look of fine lines and wrinkles. Say goodbye to acne blackheads, and breakouts and make your skin feeling deeply refreshed &amp; cleansed.</p>
    <div class="icons">
      <svg width="18" height="18" viewBox="0 0 18 18" fill="none" stroke="currentColor" stroke-width="1.4"><path d="M3 9a6 6 0 0 1 10.5-4M15 9a6 6 0 0 1-10.5 4"/><path d="M13.5 1.5v3.5H10M4.5 16.5V13H8"/></svg>
      <svg width="18" height="18" viewBox="0 0 18 18" fill="currentColor"><path d="M9 2l4 7H5z"/><path d="M3 12h12l-2 4H5z"/></svg>
      <svg width="18" height="18" viewBox="0 0 18 18" fill="none" stroke="currentColor" stroke-width="1.2"><rect x="3" y="6" width="12" height="10" rx="1"/><path d="M4 3h10v3H4z"/><text x="9" y="14" font-size="5" text-anchor="middle" fill="currentColor" stroke="none" font-family="sans-serif">18M</text></svg>
    </div>
    <p class="ingredients">Ingredients: Dead Sea Mud, Deionized Water, Kaolin, Allantoin, Shea Butter, Sunflower Oil, Aloe Vera Juice, Vegetable Glycerin, Jojoba Oil, Hickory Bark Extract, Calendula Oil, Xanthan Gum.</p>
  </div>
</section>

</body>
</html>
```